Flyer Design Project- Wine Meditation

I require a flyer to be created for a course. It is a meditation course. So I want the cover design to look quirky but calm.

I have attached a previous design. The wording on the back should be the same only any reference to Chocolate should be changed to Wine. This project is for wine meditation. Although I have attached the previous flyer for guidance of the lay out and words used, I DO NOT want to to be a direct copy, I want it to look completely different. SO be creative. Any copies or anything that looks close to a copy will not even be considered.

I want the flyer to be A5 side but also the ability to resize it onto smaller cards.

I have also attached the wording for the back of the flyer in the attached word document.

If you need further information about the design breif please contact me.

Target Market(s)

20 to 40

Requirements
Must have
• Must have space for a logo which is currently being designed by the pixel harbour. For the time being insert the silver fern hollow wellness logo which is attached.

Picture something realted to wine on the front and course detail on the back same as the attached sample.
Should not have
• a direct copy of my samples I have attached.

```html
<!DOCTYPE html>
<html lang="en">
<head>
<meta charset="utf-8">
<title>Wine Meditation Course Flyer</title>
<link rel="stylesheet" href="https://fonts.googleapis.com/css2?family=Great+Vibes&family=Open+Sans:wght@600;700&family=Arimo:wght@400;700&display=swap">
<style>
  :root {
    --page: #ffffff;
    --cream: #f4f0e6;
    --panel: #efebe0;
    --wine: #8c1424;
    --wine-deep: #5e0b17;
    --wine-bright: #a5172c;
    --ink: #2b2b2b;
    --grey: #555555;
    --rule: #c9c4b6;
  }
  * { margin: 0; padding: 0; box-sizing: border-box; }
  html, body { width: 850px; height: 1200px; overflow: hidden; }
  body { position: relative; background: var(--page); font-family: "Arimo", Arial, sans-serif; color: var(--ink); }

  .front {
    position: absolute; left: 27px; top: 38px; width: 799px; height: 562px;
    overflow: hidden; box-shadow: 0 2px 6px rgba(0,0,0,.25);
  }
  .front-photo {
    position: absolute; inset: 0;
    background:
      radial-gradient(ellipse 62% 48% at 50% 100%, var(--wine-bright) 0%, var(--wine) 55%, var(--wine-deep) 100%) bottom / 100% 52% no-repeat,
      linear-gradient(180deg, #f6f3ea 0%, var(--cream) 100%);
  }
  .front-title {
    position: absolute; left: 0; right: 0; top: 28px; text-align: center;
    font-family: "Great Vibes", cursive; font-size: 230px; line-height: 1;
    color: var(--wine); padding-right: 20px;
  }
  .front-ghost {
    position: absolute; left: 0; right: 0; top: 386px; text-align: center;
    font-family: "Open Sans", sans-serif; font-weight: 700; font-size: 118px;
    color: rgba(255,255,255,.13); letter-spacing: 1px; white-space: nowrap;
  }
  .front-subtitle {
    position: absolute; left: 0; right: 0; top: 428px; text-align: center;
    font-family: "Open Sans", sans-serif; font-weight: 700; font-size: 66px;
    color: #fbf6ec; letter-spacing: .5px;
  }

  .back {
    position: absolute; left: 27px; top: 617px; width: 799px; height: 563px;
    background: var(--page); box-shadow: 0 2px 6px rgba(0,0,0,.25);
  }
  .back-brand {
    position: absolute; left: 0; top: 0; width: 269px; height: 100%;
    text-align: center;
  }
  .brand-title {
    position: absolute; left: 0; right: 0; top: 4px;
    font-family: "Great Vibes", cursive; font-size: 96px; line-height: 1;
    color: var(--wine);
  }
  .brand-course {
    position: absolute; left: 0; right: 0; top: 104px;
    font-family: "Open Sans", sans-serif; font-weight: 700; font-size: 19.5px;
    color: var(--grey); letter-spacing: .3px;
  }
  .client-name {
    position: absolute; left: 40px; right: 40px; top: 200px;
    display: flex; flex-direction: column; align-items: center; gap: 14px;
    font-family: "Open Sans", sans-serif; font-weight: 700; font-size: 26px;
    line-height: 1.15; color: var(--grey); text-transform: uppercase;
  }
  .client-name .mark { width: 70px; height: 70px; background: var(--wine); }
  .brand-contact {
    position: absolute; left: 0; right: 0; top: 452px;
    font-family: "Open Sans", sans-serif; font-weight: 700; font-size: 11px;
    color: var(--ink); letter-spacing: .3px; line-height: 15px; text-transform: uppercase;
  }
  .brand-contact p + p { margin-top: 22px; }

  .back-details {
    position: absolute; left: 269px; top: 0; width: 530px; height: 100%;
    background: var(--panel); border-left: 1px solid var(--rule);
    padding: 52px 56px 0 30px;
  }
  .details-heading {
    font-family: "Open Sans", sans-serif; font-weight: 700; font-size: 24px;
    color: var(--wine); margin-bottom: 8px;
  }
  .details-copy { font-size: 15.5px; line-height: 18px; text-align: justify; }
  .details-sub {
    font-family: "Open Sans", sans-serif; font-weight: 700; font-size: 13.5px;
    color: var(--wine); text-transform: uppercase; margin: 28px 0 20px;
  }
  .details-list { list-style: none; font-size: 15.5px; line-height: 19.5px; }
  .details-list li { position: relative; padding-left: 17px; }
  .details-list li::before { content: "•"; position: absolute; left: 2px; }
</style>
</head>
<body>
  <section class="front">
    <div class="front-photo" role="img" aria-label="Close-up photograph of a red wine glass with a single drop falling into the wine and sending out ripples"></div>
    <h1 class="front-title">Wine</h1>
    <div class="front-ghost" aria-hidden="true">MEDITATION</div>
    <div class="front-subtitle">MEDITATION</div>
  </section>

  <section class="back">
    <aside class="back-brand">
      <div class="brand-title">Wine</div>
      <div class="brand-course">MEDITATION COURSE</div>
      <div class="client-name">
        <span class="mark"></span>
        <span>Silver Fern Hollow Wellness</span>
      </div>
      <div class="brand-contact">
        <p>www.vine-stillness.com</p>
        <p>Brought to you by<br>Silver Fern Hollow Wellness</p>
        <p>Phone (02) 5550 0148</p>
      </div>
    </aside>

    <div class="back-details">
      <h2 class="details-heading">Wine What?!</h2>
      <p class="details-copy">Yes you read right. Wine meditation! What could be better than combining the dilatable taste of wine with meditation, right? Well that is exactly what this course is all about with a little bit of Mindfulness thrown in.</p>

      <h3 class="details-sub">Learn to drink wine without the hangover!</h3>
      <p class="details-copy">NO HANGOVER! Really? It’s true because we challenge you to the fact that you have never really savoured your glass of wine. So we are going to teach you how to do it mindfully. This way you are guaranteed not to get a hangover while drinking wine.</p>

      <h3 class="details-sub">What you get with the course:</h3>
      <ul class="details-list">
        <li>A Wine Meditation course book.</li>
        <li>Mindfulness and meditation instruction online.</li>
        <li>Learn how to drink wine mindfully.</li>
        <li>Learn Meditation techniques and postures.</li>
        <li>FREE mp3 Guided Meditation download.</li>
        <li>5% of the course goes to charity –<br>Please see our website for this month’s charitable cause.</li>
      </ul>
    </div>
  </section>
</body>
</html>
```